Small consulting business needs a website designed to highlight value and four offerings

My company is a dynamic consulting firm with four Core Offerings: Learning & Evaluation, Program Management, Facilitation & Coaching; Implementation & Transformation. Our mission is to facilitate organizational change and transformation, and to make space for creativity, joy, belonging, and trust. If done successfully, we grow to better understand ourselves, each other, and the work we do together.

I'd like the website to give a feeling of confidence and clarity. I want the colors to match or compliment my logo. I want to have three tabs - Our Clients, Our Services, and Government.

See attached Word document for additional content. My current website is www.BrightHarborGroup.com.

Some websites I'm inspired by:
https://www.ovalmeadowworks.com
https://www.solvantpartnership.com
https://tqrb.org

Some websites of people/groups in my field that I find uninspiring:
http://danaquillby.com
https://www.moorvale.org

Target Market(s)

State and local government agencies, health tech, and corporate HR departments

Industry/Entity Type

public health, aging, government, health tech

Coding

Number of Pages Required

4 page

Font styles to use
Other font styles liked:
• Calibri and Merriweather

Colors
0054AA
0677BA
7BADD7
CADEEF
E8F1F8
00AB8E
00BBA5
67D7C9
C6EFE9
E9F9F6
FFC000
F8CF3A
FAE287
FDF2CF
FEFAEE
F0912C
F2A743
F7CA91
FBE8D2
FDF5EE

Requirements
Must have
• Attached logo and content, water colors few, and photos.
Nice to have
• Real pictures, which I can provide to the chosen designer
Should not have
• AI generated characters or cartoons.

```html
<!DOCTYPE html>
<html lang="en">
<head>
<meta charset="utf-8">
<title>Bright Harbor Group — Consulting</title>
<link href="https://fonts.googleapis.com/css2?family=Merriweather:wght@300;400;700&family=Carlito:wght@400;700&family=Montserrat:wght@600;700&display=swap" rel="stylesheet">
<style>
:root{
  --teal:#00bba5;
  --teal-card:#2ecbb6;
  --teal-deep:#13b9a0;
  --teal-dark:#00ab8e;
  --teal-line:#3cc9b5;
  --teal-wash:#e9f9f6;
  --orange:#ffa000;
  --gold:#ffc000;
  --gold-soft:#f8cf3a;
  --ink:#1c1c1c;
  --white:#ffffff;
  --placeholder-warm:#f3ead2;
  --placeholder-cool:#dcefe9;
}
*{box-sizing:border-box;margin:0;padding:0}
html,body{width:1200px;height:5263px;overflow:hidden}
body{position:relative;background:var(--white);color:var(--ink);font-family:"Carlito",Calibri,sans-serif}
.abs{position:absolute}

/* header / hero */
.hero{left:0;top:0;width:1200px;height:850px;
  background:
    radial-gradient(ellipse 260px 300px at 40px 180px,rgba(103,215,201,.45),transparent 70%),
    radial-gradient(ellipse 300px 220px at 120px 620px,rgba(247,202,145,.35),transparent 70%),
    radial-gradient(ellipse 300px 300px at 1170px 320px,rgba(198,239,233,.8),transparent 70%),
    radial-gradient(ellipse 260px 200px at 1000px 760px,rgba(250,226,135,.35),transparent 70%),
    var(--white);}
.brand{left:152px;top:12px;display:flex;align-items:center;gap:12px}
.brand-mark{width:62px;height:62px;border-radius:50%;background:var(--gold-soft)}
.brand-name{font-family:"Merriweather",Georgia,serif;font-weight:300;font-size:19px;line-height:29px;color:#333;text-align:center}
.nav{left:480px;top:46px;display:flex;align-items:center;gap:22px;font-family:"Montserrat",sans-serif;font-weight:700;font-size:12.5px;color:#222}
.nav .dot{width:5px;height:5px;border-radius:50%;background:var(--teal)}
.cta{left:986px;top:37px;width:140px;height:36px;border-radius:18px;background:var(--gold);color:#fff;font-family:"Montserrat",sans-serif;font-weight:700;font-size:12.5px;display:flex;align-items:center;justify-content:center}
.hero-title{left:0;top:136px;width:1200px;text-align:center;font-family:"Merriweather",Georgia,serif;font-weight:400;font-size:39px;line-height:44px;color:#111}
.hero-title b{font-weight:700}
.hero-sub{left:0;top:246px;width:1200px;text-align:center;font-size:16px;line-height:27px;color:#222}
.offer-ring{left:350px;top:333px;width:500px;height:500px;border-radius:50%;border:4px solid var(--teal-line)}
.offer-art{left:400px;top:383px;width:400px;height:400px;border-radius:50%;background:linear-gradient(180deg,var(--placeholder-warm),var(--placeholder-cool))}
.offer-icon{width:68px;height:68px;border-radius:50%;display:flex;align-items:center;justify-content:center}
.offer-icon.gold{background:var(--gold)}
.offer-icon.teal{background:var(--teal)}
.offer-icon.orange{background:var(--orange)}
.offer-label{font-family:"Merriweather",Georgia,serif;font-weight:700;font-size:18px;line-height:20px;color:#222}

/* intro */
.down{left:588px;top:884px}
.section-title{left:0;width:1200px;text-align:center;font-family:"Merriweather",Georgia,serif;font-weight:400;color:#111}
.spine{left:599px;width:2px;background:var(--teal-line)}
.card{left:123px;width:948px;border-radius:16px;color:#fff;text-align:center}
.card h2{font-family:"Merriweather",Georgia,serif;font-weight:400;font-size:36px;margin-top:68px}
.card h2 b{font-weight:700}
.card p{font-size:19px;line-height:27px;margin:18px auto 0;width:760px}
.card.mission{top:1143px;height:285px;background:var(--teal-card)}
.card.vision{top:1498px;height:286px;background:var(--orange)}
.card.value{top:1909px;height:307px;background:var(--teal-deep)}
.card.vision h2{margin-top:56px}
.card.vision p{margin-top:8px;width:680px}
.card.value h2{margin-top:58px}
.card.value p{width:780px;margin-top:12px}
.card-icon{left:556px;width:88px;height:88px;border-radius:50%;background:#fff;border:3px solid var(--teal-card);display:flex;align-items:center;justify-content:center}
.art{border-radius:12px;background:linear-gradient(180deg,var(--placeholder-warm),var(--placeholder-cool))}
.art.left{left:125px;top:2280px;width:425px;height:410px}
.art.right{left:645px;top:2262px;width:440px;height:430px}

/* help band */
.help{left:0;top:2766px;width:1200px;height:520px;background:linear-gradient(180deg,#22b3ad 0%,#0dbaa4 60%,#11b9a2 100%)}
.help h3{position:absolute;left:0;top:84px;width:1200px;text-align:center;font-family:"Merriweather",Georgia,serif;font-weight:400;font-size:42px;color:#fff}
.underline{position:absolute;height:4px;border-radius:2px}
.list{position:absolute;left:0;width:1200px;text-align:center;font-family:"Merriweather",Georgia,serif;font-weight:300;color:#fff}
.list li{list-style:none}
.help .list{top:185px}
.help .list li{font-size:28px;line-height:44px}
.help .list li:first-child{font-size:38px;line-height:54px;font-weight:400}
.fade1{opacity:.55}.fade2{opacity:.38}.fade3{opacity:.22}.fade4{opacity:.12}.fade5{opacity:.07}.fade6{opacity:.04}
.torn{position:absolute;left:0;width:1200px}

.common{left:0;top:3286px;width:1200px;height:485px;
  background:
    radial-gradient(ellipse 260px 200px at 120px 380px,rgba(198,239,233,.6),transparent 70%),
    radial-gradient(ellipse 320px 260px at 1100px 140px,rgba(251,232,210,.8),transparent 70%),
    var(--white)}
.common h3{position:absolute;left:0;top:158px;width:1200px;text-align:center;font-family:"Merriweather",Georgia,serif;font-weight:700;font-size:64px;color:#1a1a1a}

/* collaborate band */
.collab{left:0;top:3771px;width:1200px;height:580px;background:linear-gradient(180deg,#fbc74a 0%,#f9b232 60%,#f6a62a 100%)}
.collab h3{position:absolute;left:0;top:78px;width:1200px;text-align:center;font-family:"Merriweather",Georgia,serif;font-weight:400;font-size:42px;color:#fff}
.collab h3 b{font-weight:700}
.collab .list{top:180px}
.collab .list li{font-size:28px;line-height:44.5px}
.collab .list li:first-child{font-size:38px;line-height:52px;font-weight:400}

/* why us */
.why-photo{left:0;top:4405px;width:572px;height:560px;background:linear-gradient(180deg,#eadfd3,#d3ddd9)}
.why{left:630px;top:4485px;width:470px}
.why h3{font-family:"Merriweather",Georgia,serif;font-weight:400;font-size:46px;color:#111;margin-bottom:26px}
.why p{font-size:16.5px;line-height:27px;color:#222;margin-bottom:27px}

/* footer */
.footer{left:0;top:4975px;width:1200px;height:288px;background:linear-gradient(180deg,#ffffff 0%,var(--teal-wash) 40%,#dff5f1 100%)}
.f-rule{position:absolute;left:158px;width:904px;height:2px;background:#67d7c9}
.f-mark{position:absolute;left:584px;top:26px;width:56px;height:56px;border-radius:50%;background:var(--gold-soft)}
.f-name{position:absolute;left:500px;top:88px;width:224px;text-align:center;font-family:"Merriweather",Georgia,serif;font-weight:300;font-size:20px;line-height:30px;color:#222;background:#eef9f7}
.f-nav{position:absolute;top:116px;display:flex;align-items:center;gap:26px;font-family:"Montserrat",sans-serif;font-weight:700;font-size:12.5px;color:#222}
.f-nav .dot{width:5px;height:5px;border-radius:50%;background:var(--teal)}
.copy{position:absolute;left:0;top:204px;width:1200px;text-align:center;font-size:13.5px;color:#222}
.social{position:absolute;left:546px;top:232px;display:flex;gap:8px}
.social span{width:30px;height:30px;border-radius:50%}
</style>
</head>
<body>

<section class="abs hero" aria-label="Introduction">
  <div class="abs brand">
    <div class="brand-mark" aria-hidden="true"></div>
    <div class="brand-name">Bright Harbor<br>Group</div>
  </div>
  <nav class="abs nav">
    <span>HOME</span><span class="dot"></span>
    <span>OUR CLIENTS</span><span class="dot"></span>
    <span>OUR SERVICES</span><span class="dot"></span>
    <span>GOVERNMENT</span>
  </nav>
  <div class="abs cta">CONTACT US &rsaquo;</div>

  <h1 class="abs hero-title">A Seat at the Table for Collaboration,<br><b>Learning, and Meaningful Change</b></h1>
  <p class="abs hero-sub">Bright Harbor Group is a dynamic consulting firm with four Core Offerings: Learning &amp; Evaluation,<br>Program Management, Facilitation &amp; Coaching; Implementation &amp; Transformation</p>

  <div class="abs offer-ring"></div>
  <div class="abs offer-art" role="img" aria-label="Illustration of the four core offerings fitting together"></div>

  <div class="abs offer-label" style="left:256px;top:401px">LEARNING</div>
  <div class="abs offer-icon gold" style="left:381px;top:378px">
    <svg width="34" height="34" viewBox="0 0 34 34" fill="none" stroke="#fff" stroke-width="2"><path d="M17 6a8 8 0 0 0-5 14v4h10v-4a8 8 0 0 0-5-14z"/><path d="M13 28h8"/></svg>
  </div>
  <div class="abs offer-icon teal" style="left:771px;top:388px">
    <svg width="34" height="34" viewBox="0 0 34 34" fill="none" stroke="#fff" stroke-width="2"><circle cx="17" cy="17" r="6"/><circle cx="17" cy="17" r="12" stroke-dasharray="4 3"/></svg>
  </div>
  <div class="abs offer-label" style="left:853px;top:412px">IMPLEMENTATION</div>
  <div class="abs offer-label" style="left:198px;top:707px">FACILITATION</div>
  <div class="abs offer-icon teal" style="left:361px;top:683px">
    <svg width="34" height="34" viewBox="0 0 34 34" fill="none" stroke="#fff" stroke-width="2"><rect x="14" y="7" width="14" height="10" rx="2"/><path d="M6 28v-6l6-4"/><circle cx="9" cy="12" r="3"/></svg>
  </div>
  <div class="abs offer-icon orange" style="left:791px;top:658px">
    <svg width="34" height="34" viewBox="0 0 34 34" fill="none" stroke="#fff" stroke-width="2"><circle cx="17" cy="17" r="5"/><circle cx="17" cy="17" r="11" stroke-dasharray="3 3"/></svg>
  </div>
  <div class="abs offer-label" style="left:876px;top:676px">PROGRAM<br>MANAGEMENT</div>
</section>

<svg class="abs down" width="24" height="30" viewBox="0 0 24 30" fill="none" stroke="#3cc9b5" stroke-width="2.5"><path d="M12 2v24M3 18l9 9 9-9"/></svg>
<h2 class="abs section-title" style="top:950px;font-size:42px">Here for you and your team</h2>
<div class="abs spine" style="top:1026px;height:46px"></div>

<article class="abs card mission">
  <h2>Our <b>Mission</b></h2>
  <p>Our mission is to facilitate organizational change and transformation, and to make space for creativity, joy, belonging, and trust. If done successfully, we grow to better understand ourselves, each other, and the work we do together.</p>
</article>
<div class="abs spine" style="top:1370px;height:128px;background:rgba(255,255,255,.5)"></div>
<div class="abs card-icon" style="top:1098px">
  <svg width="48" height="48" viewBox="0 0 48 48" fill="none" stroke="#2ecbb6" stroke-width="2.2"><circle cx="24" cy="24" r="16"/><circle cx="24" cy="24" r="10"/><circle cx="24" cy="24" r="4"/><path d="M24 24l14-14M34 8v6h6"/></svg>
</div>

<article class="abs card vision">
  <h2>Our <b>Vision</b></h2>
  <p>Our vision is to be part of a world where organizations and collaborators connect as human beings first. We envision a future where partners and colleagues strive for ongoing growth together.</p>
</article>
<div class="abs card-icon" style="top:1461px;border-color:var(--orange)">
  <svg width="48" height="48" viewBox="0 0 48 48" fill="none" stroke="#ffa000" stroke-width="2.2"><path d="M24 12a9 9 0 0 0-6 16v5h12v-5a9 9 0 0 0-6-16z"/><path d="M20 38h8M24 4v4M10 10l3 3M38 10l-3 3"/></svg>
</div>
<div class="abs spine" style="top:1716px;height:68px;background:rgba(255,255,255,.7)"></div>
<div class="abs spine" style="top:1784px;height:80px"></div>

<article class="abs card value">
  <h2>Our <b>Value</b></h2>
  <p>We are the tranquility in chaos. The steady partner always at the table with you. We drive meaningful and measurable change, resulting in sustained progress towards key community outcomes and multi-sector initiatives. Our work produces values realignment, critical technical assistance, and develops strategic plans for innovative organizations ready to elevate their work.</p>
</article>
<div class="abs card-icon" style="top:1863px;border-color:var(--teal-deep)">
  <svg width="48" height="48" viewBox="0 0 48 48" fill="none" stroke="#13b9a0" stroke-width="2.2"><path d="M12 16h24l6 7-18 18L6 23z"/><path d="M6 23h36M18 16l6 25 6-25"/></svg>
</div>
<div class="abs spine" style="top:2186px;height:580px;background:#d7eeea;width:1px"></div>

<div class="abs art left" role="img" aria-label="Watercolor artwork representing connection and collaboration"></div>
<div class="abs art right" role="img" aria-label="Watercolor artwork representing energy and transformation"></div>

<section class="abs help" aria-label="How we help">
  <h3>We Help Your Team...</h3>
  <div class="underline" style="left:548px;top:150px;width:164px;background:#fff"></div>
  <ul class="list">
    <li>Turn bold visions into practical results.</li>
    <li class="fade1">Empower teams to be better together.</li>
    <li class="fade2">Transform conflict into opportunity.</li>
    <li class="fade3">Strengthen community-led systems.</li>
    <li class="fade4">Foster a sense of belonging...</li>
  </ul>
  <svg class="torn" style="top:470px" width="1200" height="60" viewBox="0 0 1200 60" preserveAspectRatio="none"><path fill="#fff" d="M0 30 L40 22 L70 34 L110 18 L150 30 L190 20 L240 36 L290 22 L330 32 L380 16 L430 30 L480 24 L530 38 L580 20 L630 30 L680 18 L730 34 L780 22 L830 30 L880 16 L930 32 L980 22 L1030 36 L1080 20 L1130 30 L1200 18 L1200 60 L0 60Z"/></svg>
</section>

<section class="abs common" aria-label="Common ground">
  <h3>...Find common ground.</h3>
  <div class="underline" style="left:470px;top:258px;width:270px;background:var(--gold)"></div>
</section>

<section class="abs collab" aria-label="Who we collaborate with">
  <h3>We <b>Collaborate With</b></h3>
  <div class="underline" style="left:520px;top:144px;width:230px;background:#fff"></div>
  <ul class="list">
    <li>Large-scale Companies</li>
    <li class="fade1">National and local nonprofits</li>
    <li class="fade2">State government agencies</li>
    <li class="fade3">International Partnerships &amp; Organizations</li>
    <li class="fade4">Foundations</li>
    <li class="fade5">Tribal Serving Organizations</li>
    <li class="fade6">Startups in tech</li>
  </ul>
  <svg class="torn" style="top:530px" width="1200" height="50" viewBox="0 0 1200 50" preserveAspectRatio="none"><path fill="#fff" d="M0 24 L50 16 L90 28 L140 14 L190 26 L240 18 L290 30 L340 16 L390 26 L440 12 L500 28 L560 18 L610 30 L670 16 L720 26 L780 14 L840 28 L900 18 L960 30 L1020 16 L1080 26 L1140 14 L1200 24 L1200 50 L0 50Z"/></svg>
</section>

<div class="abs why-photo" role="img" aria-label="Photo of a small team working together at a whiteboard in a bright office"></div>
<section class="abs why">
  <h3>Why Us</h3>
  <p>Through our Core Offerings and guided by our founder's traditional and nontraditional methods for engaging and steering a team, we create a sense of belonging, foster transparency, and help to build stronger relationships.</p>
  <p>Our approach helps to drive meaningful change so that organizations and initiatives can clear roadblocks and meet collective goals. Our team's proven ability to transform conflict into opportunity will help to advance your organization and the communities you serve.</p>
</section>

<footer class="abs footer">
  <div class="f-rule" style="top:95px"></div>
  <div class="f-rule" style="top:150px"></div>
  <div class="f-mark" aria-hidden="true"></div>
  <div class="f-name">Bright Harbor<br>Group</div>
  <nav class="f-nav" style="left:280px"><span>HOME</span><span class="dot"></span><span>OUR CLIENTS</span></nav>
  <nav class="f-nav" style="left:760px"><span>OUR SERVICES</span><span class="dot"></span><span>GOVERNMENT</span></nav>
  <p class="copy">&copy; 2025 Bright Harbor Group. All Right Reserved</p>
  <div class="social" aria-label="Social links">
    <span style="background:var(--gold)"></span>
    <span style="background:var(--teal)"></span>
    <span style="background:var(--teal)"></span>
    <span style="background:var(--teal)"></span>
  </div>
</footer>

</body>
</html>
```